Business card for psychiatrist

Business card design project for a psychiatristWe would like to have the impression of 1. We (patient and the doctor) are working together.2. Light the way so that patients can see where they are going and what their goals are.3. One side of the business card will have the letter "TFP" which stands for Thornvale Family Psychiatry.4. The other side of the business card will have the address, phone number, name of the psychiatrist, website, etc.5. A logo could go into either side of the business card. Let's see what looks better.
Business card design project for a psychiatrist
We would like to have the impression of
1. We (patient and the doctor) are working together.
2. Light the way so that patients can see where they are going and what their goals are.
3. One side of the business card will have the letter "TFP" which stands for Thornvale Family Psychiatry.
4. The other side of the business card will have the address, phone number, name of the psychiatrist, website, etc.
5. A logo could go into either side of the business card. Let's see what looks better.
Colors
Designer to choose colors to be used in the design.
Look and feel
Each slider illustrates characteristics of the customer's brand and the style your logo design should communicate.

```html
<!DOCTYPE html>
<html lang="en">
<head>
<meta charset="utf-8">
<title>Thornvale Family Psychiatry — Business Card</title>
<link rel="stylesheet" href="https://fonts.googleapis.com/css2?family=Arimo:wght@400&display=swap">
<style>
  :root {
    --stage: #cfcfcf;
    --paper: #ffffff;
    --green: #8bc040;
    --blue: #2ea2db;
    --ink: #1a1a1a;
  }
  * { margin: 0; padding: 0; box-sizing: border-box; }
  html, body { width: 1200px; height: 900px; overflow: hidden; }
  body {
    background: var(--stage);
    font-family: "Arimo", Arial, sans-serif;
    position: relative;
  }
  .card {
    position: absolute;
    width: 652px;
    height: 372px;
    overflow: hidden;
  }
  .card--front { left: 274px; top: 57.5px; background: var(--paper); }
  .card--back  { left: 278px; top: 483px; background: var(--green); }

  .front-swoosh { position: absolute; left: 0; top: 0; width: 652px; height: 372px; }

  .brand-mark {
    position: absolute;
    display: flex;
    align-items: center;
    gap: 12px;
  }
  .brand-mark__dot { border-radius: 50%; flex: none; }
  .brand-mark__name { font-weight: 400; line-height: 1; letter-spacing: 1px; }

  .card--front .brand-mark { left: 108px; top: 160px; }
  .card--front .brand-mark__dot { width: 56px; height: 56px; background: var(--blue); }
  .card--front .brand-mark__name { font-size: 50px; color: var(--green); }

  .divider {
    position: absolute;
    left: 326px; top: 95px;
    width: 2px; height: 185px;
    background: var(--green);
  }

  .contact-block { position: absolute; left: 352px; top: 86px; color: var(--ink); }
  .contact-block__name { font-size: 29.5px; color: var(--green); line-height: 1; }
  .contact-block__role { font-size: 14px; margin-top: 3px; line-height: 1; }
  .contact-block__rule { width: 28px; height: 2px; background: var(--green); margin: 7px 0 8px; }
  .contact-block__address { font-size: 13.2px; line-height: 16.5px; }
  .contact-list { list-style: none; margin-top: 1px; }
  .contact-list__item {
    display: flex; align-items: center; gap: 6px;
    font-size: 13.2px; height: 23.5px;
  }
  .contact-list__icon { width: 16px; height: 16px; flex: none; }

  .card--back .brand-mark { left: 0; right: 0; top: 145px; justify-content: center; }
  .card--back .brand-mark__dot { width: 56px; height: 56px; background: var(--paper); }
  .card--back .brand-mark__name { font-size: 50px; color: var(--paper); }

  .practice-band {
    position: absolute;
    left: 0; top: 311px;
    width: 652px; height: 40px;
    background: var(--blue);
    color: var(--paper);
    font-size: 26px;
    display: flex; align-items: center; justify-content: center;
  }
</style>
</head>
<body>

<section class="card card--front">
  <svg class="front-swoosh" viewBox="0 0 652 372" aria-hidden="true">
    <path d="M0 305.5 Q326 375.5 652 305.5 L652 372 L0 372 Z" fill="var(--green)"/>
    <path d="M65 308.5 Q324 341.5 583 308.5 Q324 359.5 65 308.5 Z" fill="var(--blue)"/>
  </svg>

  <div class="brand-mark">
    <span class="brand-mark__dot"></span>
    <span class="brand-mark__name">TFP</span>
  </div>

  <div class="divider"></div>

  <div class="contact-block">
    <h1 class="contact-block__name" style="font-weight:400">Marisa Van Heerden</h1>
    <p class="contact-block__role">Director</p>
    <div class="contact-block__rule"></div>
    <p class="contact-block__address">Unit 12, Lindell Court, Acacia Rd,<br>Glenmore AH, Halfway Vale, 1734</p>
    <div class="contact-block__rule"></div>
    <ul class="contact-list">
      <li class="contact-list__item">
        <svg class="contact-list__icon" viewBox="0 0 16 16" aria-hidden="true"><path d="M3 1.5 L6 4.5 L4.5 6.5 Q6.5 10 9.5 11.5 L11.5 10 L14.5 13 L12.5 15 Q6 14 1 4 Z" fill="var(--green)"/></svg>
        <span>010 555 2184</span>
      </li>
      <li class="contact-list__item">
        <svg class="contact-list__icon" viewBox="0 0 16 16" aria-hidden="true"><path d="M3 1.5 L6 4.5 L4.5 6.5 Q6.5 10 9.5 11.5 L11.5 10 L14.5 13 L12.5 15 Q6 14 1 4 Z" fill="var(--green)"/></svg>
        <span>076 555 9032</span>
      </li>
      <li class="contact-list__item">
        <svg class="contact-list__icon" viewBox="0 0 16 16" aria-hidden="true"><rect x="1" y="3.5" width="14" height="9" fill="var(--green)"/><path d="M1 3.5 L8 9 L15 3.5 M1 12.5 L6 7.5 M15 12.5 L10 7.5" stroke="#fff" stroke-width="1" fill="none"/></svg>
        <span>marisa@brightpathcare.org.za</span>
      </li>
      <li class="contact-list__item">
        <svg class="contact-list__icon" viewBox="0 0 16 16" aria-hidden="true"><circle cx="8" cy="8" r="7" fill="none" stroke="var(--green)" stroke-width="1.4"/><path d="M1 8 H15 M8 1 Q4 8 8 15 Q12 8 8 1" fill="none" stroke="var(--green)" stroke-width="1.2"/></svg>
        <span>www.brightpathcare.org.za</span>
      </li>
    </ul>
  </div>
</section>

<section class="card card--back">
  <div class="brand-mark">
    <span class="brand-mark__dot"></span>
    <span class="brand-mark__name">TFP</span>
  </div>
  <div class="practice-band">Thornvale Family Psychiatry</div>
</section>

</body>
</html>
```